Cover Art Design for a Notebook

We are going to give away some note books to our marketing department and want an elegant art design for the cover. There is a theme centered around ABCD of marketing that we want to leverage in the design. So these letters should be prominent in the design. The ABCD stand for Agility, Boost, Customer, Data.

If you could Cleverly incorporate these words into the letters with a good design that would be good.

But please make the ABCD the focus of the artwork. The words associated with them should be subtle, in the background, visible but not the focus.

We are looking for stylish. We want people to feel proud of the ELEGANT DESIGN when they take out this notebook for business.

Also worth mentioning- We are a biotechnology company so if you incorporate elements in that theme in, on, or around the ABCD letters, it could be a good idea. As long as it doesn’t kill the rest of the design.

I will upload our logo for Veltrane Orwick Biologics later (you can see it online) and this will need to go in one corner.

Notebook will be A5 format. Image on front cover only. Need ASAP.

(Do not make baby blocks as we don’t want something that looks like a kids book)

Target Market(s)

business people who feel proud to pull out this notebook

Industry/Entity Type

Biotechnology

Colors
ec1f27
ffffff
000000

Requirements
Must have
• ELEGANT ART DESIGN USING ABCD
Nice to have
• see brief above
Should not have
• baby blocks

```html
<!DOCTYPE html>
<html lang="en">
<head>
<meta charset="utf-8">
<title>ABCD Notebook Cover – Veltrane Orwick Biologics</title>
<link rel="stylesheet" href="https://fonts.googleapis.com/css2?family=Arimo:wght@400;700&display=swap">
<style>
  :root {
    --brand-red: #ec1f27;
    --ink: #2a2a2a;
    --frame-white: #ffffff;
    --haze-peach: #f6d2c4;
    --haze-pink: #e7b8c4;
    --haze-grey: #dcdad8;
    --glass-amber: #e9a27f;
    --glass-rose: #f1b6b0;
  }
  * { margin: 0; padding: 0; box-sizing: border-box; }
  html, body { width: 846px; height: 1200px; overflow: hidden; background: #fff; }
  .cover {
    position: relative;
    width: 846px;
    height: 1200px;
    overflow: hidden;
    font-family: "Arimo", Arial, sans-serif;
  }
  .cover__backdrop { position: absolute; inset: 0; }
  .cover__graphic { position: absolute; inset: 0; }
  .brand {
    position: absolute;
    left: 73px;
    top: 104px;
    width: 284px;
    text-align: center;
    color: var(--brand-red);
    font-weight: 700;
    font-size: 27px;
    line-height: 30px;
    letter-spacing: -0.5px;
  }
  .hex-letter {
    font-family: "Arimo", Arial, sans-serif;
    font-weight: 400;
    font-size: 158px;
    fill: var(--brand-red);
  }
  .hex-word {
    font-family: "Arimo", Arial, sans-serif;
    font-weight: 400;
    font-size: 42px;
    fill: var(--ink);
    letter-spacing: -0.5px;
  }
  .hex-frame {
    fill: rgba(255, 255, 255, 0.12);
    stroke: var(--frame-white);
    stroke-width: 4;
  }
  .connector { stroke: var(--frame-white); stroke-width: 4; }
</style>
</head>
<body>
<main class="cover">
  <svg class="cover__backdrop" width="846" height="1200" viewBox="0 0 846 1200" role="img" aria-label="Soft-focus photograph of a clear laboratory well plate glowing in warm pink and amber light">
    <defs>
      <linearGradient id="backdrop-fade" x1="0" y1="0" x2="0" y2="1">
        <stop offset="0" stop-color="#ecd3c8"/>
        <stop offset="0.22" stop-color="var(--haze-peach)"/>
        <stop offset="0.5" stop-color="var(--haze-grey)"/>
        <stop offset="0.72" stop-color="#e8cfcd"/>
        <stop offset="0.86" stop-color="var(--glass-rose)"/>
        <stop offset="1" stop-color="var(--glass-amber)"/>
      </linearGradient>
      <radialGradient id="backdrop-glow" cx="0.05" cy="0.15" r="0.45">
        <stop offset="0" stop-color="#d88fa6" stop-opacity="0.6"/>
        <stop offset="1" stop-color="#d88fa6" stop-opacity="0"/>
      </radialGradient>
    </defs>
    <rect width="846" height="1200" fill="url(#backdrop-fade)"/>
    <rect width="846" height="1200" fill="url(#backdrop-glow)"/>
  </svg>

  <svg class="cover__graphic" width="846" height="1200" viewBox="0 0 846 1200" aria-hidden="true">
    <line class="connector" x1="211" y1="185" x2="211" y2="272"/>
    <line class="connector" x1="583" y1="914" x2="643" y2="974"/>

    <g class="hex-cell">
      <polygon class="hex-frame" points="211,272 330,341 330,479 211,548 92,479 92,341"/>
      <text class="hex-letter" x="211" y="428" text-anchor="middle">A</text>
      <text class="hex-word" x="209" y="480" text-anchor="middle">Agile</text>
    </g>
    <g class="hex-cell">
      <polygon class="hex-frame" points="338,489 457,558 457,696 338,765 219,696 219,558"/>
      <text class="hex-letter" x="347" y="646" text-anchor="middle">B</text>
      <text class="hex-word" x="341" y="697" text-anchor="middle">Boost</text>
    </g>
    <g class="hex-cell">
      <polygon class="hex-frame" points="591,489 710,558 710,696 591,765 472,696 472,558"/>
      <text class="hex-letter" x="590" y="646" text-anchor="middle">C</text>
      <text class="hex-word" x="598" y="697" text-anchor="middle">Customer</text>
    </g>
    <g class="hex-cell">
      <polygon class="hex-frame" points="464,706 583,775 583,913 464,982 345,913 345,775"/>
      <text class="hex-letter" x="472" y="861" text-anchor="middle">D</text>
      <text class="hex-word" x="462" y="915" text-anchor="middle">Data</text>
    </g>
  </svg>

  <div class="brand">Veltrane Orwick<br>Biologics</div>
</main>
</body>
</html>
```